Creative Businesss Card desgin!

Create a business card for our business Gleam window cleaning!
We are open to creative ideas as long as it maintains a professional image.

Target Market(s)

Small Commercial window cleaning clients including car dealerships, strata manager, cafe

Industry/Entity Type

Window Cleaning

Contact Information for Business Card

Daniel Prescott
General Manager
Gleam Window Cleaning

daniel@gleamservices.com.au
pane-care-southbank.com.au
Ph: 1800 GET GLEAM
Mob: 0437 582 061

Colors
fbed22
0392cd

Requirements
Should not have
• Stock window cleaning/ squeegee graphics

```html
<!DOCTYPE html>
<html lang="en">
<head>
<meta charset="utf-8">
<title>Gleam Window Cleaning – Business Card</title>
<link rel="stylesheet" href="https://fonts.googleapis.com/css2?family=Exo+2:wght@400;600&display=swap">
<style>
  :root {
    --backdrop: #2a2c2f;
    --card-blue: #0392cd;
    --gleam-yellow: #fbed22;
    --card-radius: 27px;
  }
  * { box-sizing: border-box; margin: 0; padding: 0; }
  html, body {
    width: 1200px;
    height: 1141px;
    overflow: hidden;
    background: var(--backdrop);
    font-family: "Exo 2", Arial, sans-serif;
    color: var(--gleam-yellow);
  }
  .card {
    position: absolute;
    left: 232px;
    width: 730px;
    height: 414px;
    background: var(--card-blue);
    border-radius: var(--card-radius);
  }
  .card--front { top: 119px; }
  .card--back { top: 570px; }

  .holder { position: absolute; left: 42px; top: 40px; }
  .holder__name { font-size: 25px; font-weight: 600; line-height: 1.1; }
  .holder__title { font-size: 15px; font-weight: 400; margin-top: 1px; }

  .company-line {
    position: absolute; left: 42px; top: 176px;
    font-size: 16px; font-weight: 400;
  }

  .contact-list {
    position: absolute; left: 42px; top: 280px;
    list-style: none;
  }
  .contact-list li {
    display: flex; align-items: center;
    height: 24.5px;
    font-size: 17px; font-weight: 400;
  }
  .contact-list svg {
    width: 13px; height: 13px;
    margin-right: 14px;
    fill: var(--gleam-yellow);
    flex: none;
  }

  .wordmark {
    position: absolute;
    display: flex; flex-direction: column; align-items: center;
    font-weight: 600;
    color: var(--gleam-yellow);
    line-height: 1;
  }
  .wordmark__name { font-size: 104px; letter-spacing: 2px; }
  .wordmark__tag { font-size: 33px; letter-spacing: 0.5px; margin-top: 6px; }

  .card--front .wordmark { right: 45px; top: 145px; }
  .card--back .wordmark { left: 0; right: 0; top: 120px; }

  .back-url {
    position: absolute; left: 0; right: 0; top: 350px;
    text-align: center;
    font-size: 17px; font-weight: 400;
  }
</style>
</head>
<body>

<section class="card card--front">
  <div class="holder">
    <p class="holder__name">Daniel Prescott</p>
    <p class="holder__title">General Manager</p>
  </div>

  <p class="company-line">Gleam Window Cleaning</p>

  <ul class="contact-list">
    <li>
      <svg viewBox="0 0 16 16" aria-hidden="true"><path d="M2 6c0-2 2-3 6-3s6 1 6 3v1h-3V5.5H5V7H2z"/><path d="M3 8h10l1 6H2z"/></svg>
      1800 GET GLEAM
    </li>
    <li>
      <svg viewBox="0 0 16 16" aria-hidden="true"><path d="M4 0h8a1 1 0 0 1 1 1v14a1 1 0 0 1-1 1H4a1 1 0 0 1-1-1V1a1 1 0 0 1 1-1zm1 2v10h6V2zm3 11a1 1 0 1 0 0 2 1 1 0 0 0 0-2z"/></svg>
      0437 582 061
    </li>
    <li>
      <svg viewBox="0 0 16 16" aria-hidden="true"><path d="M0 3h16v1.5L8 9 0 4.5z"/><path d="M0 6.3l8 4.5 8-4.5V13H0z"/></svg>
      daniel@gleamservices.com.au
    </li>
    <li>
      <svg viewBox="0 0 16 16" aria-hidden="true"><path d="M8 0a8 8 0 1 0 0 16A8 8 0 0 0 8 0zm-1 3 2 1-1 2 2 1v2l-2 2-1 2-1-3-2-1v-2l2-1z"/></svg>
      pane-care-southbank.com.au
    </li>
  </ul>

  <div class="wordmark">
    <span class="wordmark__name">GLEAM</span>
    <span class="wordmark__tag">WINDOW CLEANING</span>
  </div>
</section>

<section class="card card--back">
  <div class="wordmark">
    <span class="wordmark__name">GLEAM</span>
    <span class="wordmark__tag">WINDOW CLEANING</span>
  </div>
  <p class="back-url">pane-care-southbank.com.au</p>
</section>

</body>
</html>
```